PowerPoint/Keynote Design Project - Quorvel

I need a fairly straightforward design for a presentation I currently use in Keynote. It is very basic, as I developed it in an Excel spreadsheet and a friend helped migrate it over to Keynote.
I don't want it to be overly complex and I don't want it to be too busy. It should not contain too many distracting elements, but I think it needs some professional design changes to make it more appealing to the eye. I think colors should be soft and not flashy; transitions should be simple.
==================================
In response to several questions received, I have added two files. One file is the actual presentation I currently use. I run it in Keynote but I uploaded it in Powerpoint. As you can see, it is a single page but it is developed sequentially.
The other file (Examples) is just a random selection of slides I chose from several unrelated presentations I use. I am providing this to illustrate the range of colors, type styles, and combinations I frequently use. However, this isn't meant to limit the choice of colors you might recommend. I am open to any colors which might enhance the overall effect of the presentation without overpowering its message.
Thank you for all the comments and questions I have received thus far.

```html
<!DOCTYPE html>
<html lang="en">
<head>
<meta charset="utf-8">
<title>Quorvel – The Path of Salvation</title>
<link href="https://fonts.googleapis.com/css2?family=PT+Sans:wght@400;700&display=swap" rel="stylesheet">
<style>
  :root {
    --red: #e0141b;
    --blue-label: #2b9ed6;
    --blue-deep: #1a7ea6;
    --bar: #c7c9cb;
    --bar-edge: #a9abad;
    --ink: #333;
    --white: #ffffff;
    --sky-1: #ffffff;
    --sky-2: #e3f3fb;
    --sky-3: #6fc3ea;
    --sky-4: #1a72c9;
    --green: #6ab42d;
    --teal: #2fa8dd;
    --crimson: #c2163f;
  }
  html, body { margin: 0; padding: 0; overflow: hidden; }
  body { width: 1200px; height: 898px; font-family: "PT Sans", sans-serif; }
  .slide {
    position: relative; width: 1200px; height: 898px; overflow: hidden;
    background: linear-gradient(180deg, var(--sky-1) 0%, var(--sky-1) 35%, var(--sky-2) 55%, #bfe4f6 75%, var(--sky-3) 100%);
  }
  .backdrop-swirl {
    position: absolute; left: 0; top: 440px; width: 1200px; height: 458px;
    background:
      radial-gradient(ellipse 520px 120px at 600px 180px, rgba(26,114,201,.75), rgba(26,114,201,0) 70%),
      radial-gradient(ellipse 700px 90px at 300px 390px, rgba(30,110,210,.55), rgba(30,110,210,0) 70%),
      radial-gradient(ellipse 500px 140px at 1050px 330px, rgba(255,255,255,.7), rgba(255,255,255,0) 70%);
  }
  .diagram { position: absolute; inset: 0; }
  .label { position: absolute; margin: 0; white-space: nowrap; transform: translateX(-50%); }
  .stage-title { color: var(--red); font-weight: 700; font-size: 29px; line-height: 1; }
  .stage-title--mid { font-size: 25px; }
  .stage-note { color: var(--ink); font-size: 13px; }
  .stage-sub { color: var(--blue-label); font-weight: 700; font-size: 16px; }
  .life-event { color: var(--blue-label); font-weight: 700; font-size: 19px; }
  .track-caption { color: var(--white); font-weight: 700; font-size: 14px; text-shadow: 0 1px 2px rgba(0,0,0,.5); }
  .banner-text { color: var(--blue-deep); font-weight: 700; font-size: 23px; }
  .cloud-text { position: absolute; color: var(--white); font-size: 15px; text-align: center; line-height: 32px; transform: translateX(-50%); }
  .cloud-text b { font-weight: 700; }
  .figure { position: absolute; border-radius: 46% 46% 12px 12px; }
  .figure--birth { left: 188px; top: 323px; width: 96px; height: 106px; background: linear-gradient(180deg, #8fd14a, var(--green)); }
  .figure--new { left: 344px; top: 323px; width: 97px; height: 106px; background: linear-gradient(180deg, #55c1ee, var(--teal)); }
  .figure--glory { left: 938px; top: 323px; width: 96px; height: 106px; background: linear-gradient(180deg, #e23a5c, var(--crimson)); }
  .figure--free { left: 648px; top: 645px; width: 100px; height: 118px; background: var(--white); border-radius: 50% 50% 14px 14px; }
</style>
</head>
<body>
<main class="slide">
  <div class="backdrop-swirl"></div>

  <svg class="diagram" width="1200" height="898" viewBox="0 0 1200 898" aria-hidden="true">
    <!-- cross -->
    <rect x="75" y="241" width="22" height="162" fill="var(--red)"/>
    <rect x="28" y="286" width="117" height="23" fill="var(--red)"/>
    <!-- timeline -->
    <rect x="33" y="403" width="1110" height="19" fill="var(--bar)" stroke="var(--bar-edge)"/>
    <polyline points="1120,388 1158,412 1120,436" fill="none" stroke="var(--bar)" stroke-width="14"/>
    <!-- stage markers -->
    <line x1="394" y1="161" x2="394" y2="618" stroke="var(--bar)" stroke-width="5"/>
    <polygon points="381,608 394,629 407,608" fill="var(--bar)"/>
    <line x1="986" y1="161" x2="986" y2="618" stroke="var(--bar)" stroke-width="5"/>
    <polygon points="973,608 986,629 999,608" fill="var(--bar)"/>
    <rect x="832" y="323" width="152" height="6" fill="var(--bar)"/>
    <!-- growth line -->
    <polyline fill="none" stroke="var(--red)" stroke-width="4" stroke-linejoin="round"
      points="398,572 436,551 467,563 483,520 534,536 551,495 581,506 614,481 661,497 713,483 741,464 769,476 816,461 837,473 853,459 872,455 886,459 919,445 975,425"/>
    <!-- banner -->
    <path d="M403,581 L975,583 L950,614 L975,645 L403,645 L430,613 Z" fill="#d2d4d6" stroke="#b3b5b7"/>
    <!-- clouds -->
    <g fill="#3aa6e3" stroke="var(--white)" stroke-width="5">
      <path d="M300,700 C290,665 340,650 365,668 C380,640 440,642 455,672 C490,668 500,700 480,720 C500,745 480,790 445,780 C420,805 360,800 345,782 C300,795 260,760 285,735 C265,720 275,700 300,700 Z"/>
      <path d="M900,700 C890,665 940,650 965,668 C980,640 1040,642 1055,672 C1090,668 1100,700 1080,720 C1100,745 1080,790 1045,780 C1020,805 960,800 945,782 C900,795 860,760 885,735 C865,720 875,700 900,700 Z"/>
    </g>
  </svg>

  <h2 class="label stage-title" style="left:400px; top:128px;">Justification</h2>
  <h2 class="label stage-title" style="left:983px; top:128px;">Glorification</h2>
  <h2 class="label stage-title stage-title--mid" style="left:655px; top:203px;">Sanctification</h2>
  <p class="label stage-note" style="left:649px; top:232px;">(Process of yielding to the Guidance and Empowerment of the Holy Spirit)</p>
  <p class="label stage-sub" style="left:663px; top:256px;">(Discipleship)</p>
  <p class="label life-event" style="left:248px; top:297px;">Physical Birth</p>
  <p class="label life-event" style="left:900px; top:297px;">Physical Death</p>
  <p class="label track-caption" style="left:689px; top:430px;">Submission / Good Works / Obedience</p>
  <p class="label banner-text" style="left:689px; top:597px;">Freedom from the Power of Sin</p>

  <div class="figure figure--birth" role="img" aria-label="Green person icon marking physical birth"></div>
  <div class="figure figure--new" role="img" aria-label="Blue person icon marking justification"></div>
  <div class="figure figure--glory" role="img" aria-label="Crimson person icon marking physical death and glorification"></div>
  <div class="figure figure--free" role="img" aria-label="White person icon with raised arms celebrating freedom"></div>

  <p class="cloud-text" style="left:383px; top:680px; margin:0;"><b>Freedom</b> from<br>The <b>Penalty</b> for<br><b>SIN</b></p>
  <p class="cloud-text" style="left:983px; top:689px; margin:0; line-height:27px;"><b>Freedom</b> from<br>The <b>Presence</b> of<br><b>SIN</b></p>
</main>
</body>
</html>
```